Logo + Design for Medical Scrubs Shopify Site

We are looking for a Shopify design for our California-based medical scrubs retail company, "Lumen Wearwell". Our scrubs have a tailored fit and use breathable, modern fabrics.

We would like to see the logo based around the colors yellow (primary) and blue (secondary). The Shopify site should have a white base while ideally utilizing accents with the primary and secondary colors.

The final design should communicate optimism & warmth along with cleanliness and order.

Target Market(s)

Younger, web-savvy nurses both Male & Female

Industry/Entity Type

Retail

Logo Text

Lumen Wearwell

Logo styles of interest
Pictorial/Combination Logo
Abstract Logo
Font styles to use
Sans Serif

Colors
fbed22
0255a3
ffffff

Requirements
Nice to have
• See www.tovandrel.com which is a competitor's site.

```html
<!DOCTYPE html>
<html lang="en">
<head>
<meta charset="utf-8">
<title>Lumen Wearwell — Medical Scrubs</title>
<link href="https://fonts.googleapis.com/css2?family=Open+Sans:wght@400;600;700;800&family=Oswald:wght@400;500;600&display=swap" rel="stylesheet">
<style>
:root{
  --yellow:#fbed22;
  --blue:#0255a3;
  --blue-dark:#013f7a;
  --blue-light:#dcebf8;
  --white:#ffffff;
  --ink:#333a44;
  --muted:#7b838e;
  --line:#e3e7ec;
  --red:#d8262e;
}
*{box-sizing:border-box;margin:0;padding:0}
html,body{width:1200px;height:2168px;overflow:hidden}
body{font-family:"Open Sans",sans-serif;color:var(--ink);background:var(--white);font-size:13px}
.wrap{width:1040px;margin:0 auto;position:relative}

/* header */
.site-header{height:96px}
.site-header .wrap{display:flex;align-items:center;height:96px;justify-content:space-between}
.brand{display:flex;align-items:center;gap:10px;font-weight:800;font-size:26px;color:var(--blue);line-height:1}
.brand-dot{width:22px;height:22px;border-radius:50%;background:var(--yellow)}
.header-right{display:flex;flex-direction:column;align-items:flex-end;gap:12px}
.top-row{display:flex;gap:26px;align-items:center;font-size:12px}
.free-ship{font-family:Oswald,sans-serif;font-weight:600;color:var(--blue);font-size:15px;letter-spacing:.5px}
.top-links a{color:var(--muted);text-decoration:none;margin-left:14px}
.bottom-row{display:flex;gap:16px;align-items:center}
.phone{color:var(--red);font-weight:700;font-size:15px;display:flex;gap:6px;align-items:center}
.search{width:190px;height:28px;border:1px solid var(--line);display:flex;align-items:center;justify-content:space-between;padding:0 8px;color:#aab;font-size:11px}
.acct{display:flex;gap:10px}
.acct span{background:var(--blue);color:#fff;font-size:11px;padding:6px 10px}

/* nav */
.main-nav{border-top:1px solid var(--line);border-bottom:3px solid var(--blue);height:38px}
.main-nav ul{list-style:none;display:flex;height:35px;width:1040px;margin:0 auto}
.main-nav li{padding:0 17px;line-height:35px;font-size:11px;font-weight:700;color:var(--blue);text-transform:uppercase}
.main-nav li.active{background:var(--blue);color:#fff}

/* hero */
.hero{height:346px;position:relative;background:linear-gradient(180deg,#eaf3fb 0%,#bcd9f1 100%);overflow:hidden}
.hero-band{position:absolute;left:0;right:0;top:0;height:78px;background:var(--yellow)}
.hero-photo{position:absolute;left:210px;top:10px;width:780px;height:240px;background:linear-gradient(180deg,#9ec7e8,#d7e8f5);border-radius:4px}
.hero-copy{position:absolute;left:0;right:0;top:250px;text-align:center}
.hero-copy h1{font-family:Oswald,sans-serif;font-weight:500;font-size:28px;color:var(--blue-dark);letter-spacing:.5px}
.hero-copy h2{font-family:Oswald,sans-serif;font-weight:500;font-size:28px;color:var(--white);background:var(--blue);display:inline-block;padding:0 14px;margin-top:2px}
.btn{display:inline-block;background:var(--red);color:#fff;font-size:10px;font-weight:700;padding:7px 14px;text-transform:uppercase}
.hero .btn{margin-top:10px}
.arrow{position:absolute;top:150px;width:30px;height:30px;background:rgba(0,0,0,.25);display:flex;align-items:center;justify-content:center}
.arrow.l{left:20px}.arrow.r{right:20px}

/* categories */
.cats{display:flex;gap:40px;justify-content:center;margin-top:22px}
.cat{width:240px;height:246px;position:relative;border:1px solid var(--line)}
.cat-img{height:100%;background:linear-gradient(160deg,#f2f4f7,#c8d9ea)}
.cat span{position:absolute;left:0;right:0;bottom:0;background:var(--blue);color:#fff;font-size:16px;font-weight:600;padding:8px 12px}

/* section heads */
.sec-title{text-align:center;font-family:Oswald,sans-serif;font-weight:500;font-size:32px;color:#222;position:relative}
.sec-title::after{content:"";display:block;width:60px;height:3px;background:var(--blue);margin:6px auto 0}

/* products */
.featured{margin-top:34px}
.products{display:flex;justify-content:space-between;width:980px;margin:28px auto 0;position:relative}
.prod{width:210px;text-align:center;font-size:10px}
.prod-img{height:240px;margin-bottom:10px}
.prod p{color:var(--ink);line-height:1.4}
.price{display:flex;justify-content:space-between;margin-top:6px;font-weight:700;color:var(--blue)}
.price s{color:var(--muted);font-weight:400}
.p-arrow{position:absolute;top:110px;color:#999;font-size:26px}
.p-arrow.l{left:-40px}.p-arrow.r{right:-40px}

/* promos */
.promos{display:flex;gap:40px;width:780px;margin:18px auto 0}
.promo{flex:1;height:170px;position:relative;border:1px solid var(--line);background:linear-gradient(90deg,#cfe1f1 0%,#fff 55%)}
.promo.right{background:linear-gradient(270deg,#cfe1f1 0%,#fff 55%)}
.promo-text{position:absolute;top:30px;right:16px;width:180px;text-align:center}
.promo.right .promo-text{left:16px;right:auto}
.promo-text h3{color:var(--red);font-size:18px;font-weight:700;line-height:1.15}
.promo-text p{color:var(--ink);font-size:11px;margin:6px 0 10px}

/* about */
.about{margin-top:38px}
.about p{width:1020px;margin:14px auto 0;font-size:10px;line-height:1.6;text-align:center;color:var(--muted)}

.why{width:860px;margin:18px auto 0;border:1px solid var(--line);height:118px;display:flex;align-items:center;padding:0 24px;gap:30px}
.why-badge{width:56px;height:56px;border-radius:50%;background:var(--blue-light)}
.why h3{font-family:Oswald,sans-serif;font-weight:500;font-size:18px;width:190px;color:#222}
.why ul{list-style:none;font-size:10px;line-height:1.8;color:var(--muted);flex:1}
.why li::before{content:"";display:inline-block;width:6px;height:6px;background:var(--blue);margin-right:6px}

/* brands */
.brands{margin-top:34px}
.brand-row{display:flex;justify-content:space-between;width:980px;margin:26px auto 0;align-items:center}
.brand-row span{font-weight:700;font-size:20px;color:var(--blue)}

/* newsletter */
.newsletter{margin-top:40px;background:var(--yellow);height:102px}
.newsletter .wrap{display:flex;align-items:center;height:102px;justify-content:space-between}
.nl-title{display:flex;gap:14px;align-items:center}
.nl-title h3{font-size:18px;font-weight:800;color:var(--blue);text-transform:uppercase}
.nl-title p{font-size:10px;color:var(--ink)}
.nl-form{display:flex}
.nl-form div{width:420px;height:34px;background:#fff}
.nl-form span{background:var(--blue-dark);color:#fff;font-size:11px;font-weight:700;padding:0 14px;line-height:34px}

/* footer */
.site-footer{background:var(--blue);height:210px;color:#fff}
.site-footer .wrap{display:flex;justify-content:space-between;padding-top:30px}
.f-col h4{font-size:13px;font-weight:700;margin-bottom:10px;text-transform:uppercase}
.f-col li{list-style:none;font-size:10px;line-height:2;color:#cfe0f1}
.f-col{width:200px}
.socials{display:flex;gap:6px}
.socials i{width:22px;height:22px;background:#fff;opacity:.9;display:block}
.copyright{background:var(--blue-dark);height:40px;color:#cfe0f1;font-size:10px;text-align:center;line-height:40px}
</style>
</head>
<body>

<header class="site-header">
  <div class="wrap">
    <div class="brand"><span class="brand-dot"></span>Lumen Wearwell</div>
    <div class="header-right">
      <div class="top-row">
        <span class="free-ship">FREE SHIPPING</span>
        <span class="top-links"><a>My Account</a><a>Wishlist</a><a>Checkout</a><a>Log In</a></span>
      </div>
      <div class="bottom-row">
        <span class="phone">
          <svg width="14" height="14" viewBox="0 0 24 24"><path fill="#d8262e" d="M6.6 10.8a15 15 0 0 0 6.6 6.6l2.2-2.2c.3-.3.7-.4 1-.2 1.1.4 2.3.6 3.6.6.6 0 1 .4 1 1V20c0 .6-.4 1-1 1A17 17 0 0 1 3 4c0-.6.4-1 1-1h3.5c.6 0 1 .4 1 1 0 1.3.2 2.5.6 3.6.1.3 0 .7-.2 1z"/></svg>
          800-555-0147
        </span>
        <div class="search">Search products...
          <svg width="12" height="12" viewBox="0 0 24 24"><circle cx="10" cy="10" r="7" fill="none" stroke="#888" stroke-width="2.5"/><path d="M15 15l6 6" stroke="#888" stroke-width="2.5"/></svg>
        </div>
        <div class="acct"><span>Cart (0)</span></div>
      </div>
    </div>
  </div>
</header>

<nav class="main-nav">
  <ul>
    <li class="active">Women</li><li>Men</li><li>New Styles</li><li>Top Sellers</li><li>Footwear &amp; Socks</li><li>Accessories</li><li>Sale</li><li>Blog &amp; News</li><li>Contact Us</li>
  </ul>
</nav>

<section class="hero">
  <div class="hero-band"></div>
  <div class="hero-photo" role="img" aria-label="Three smiling healthcare workers wearing scrubs and a white coat"></div>
  <div class="hero-copy">
    <h1>"FASHION THAT STARTS WITH A SMILE"</h1>
    <h2>THE MOST POPULAR SCRUBS</h2><br>
    <span class="btn">Shop Now</span>
  </div>
  <div class="arrow l"><svg width="10" height="14"><path d="M8 1L2 7l6 6" stroke="#fff" stroke-width="2" fill="none"/></svg></div>
  <div class="arrow r"><svg width="10" height="14"><path d="M2 1l6 6-6 6" stroke="#fff" stroke-width="2" fill="none"/></svg></div>
</section>

<section class="cats">
  <div class="cat"><div class="cat-img" role="img" aria-label="Two nurses in purple and pink scrubs"></div><span>Hot New Colors</span></div>
  <div class="cat"><div class="cat-img" role="img" aria-label="Two clinicians in green scrubs"></div><span>Built to Last...</span></div>
  <div class="cat"><div class="cat-img" role="img" aria-label="Nurse in pink scrubs"></div><span>Be Ultra Flexible</span></div>
</section>

<section class="featured">
  <h2 class="sec-title">Fetures Product</h2>
  <div class="products">
    <span class="p-arrow l">&#8249;</span>
    <div class="prod">
      <div class="prod-img" role="img" aria-label="Plum scrub pants" style="background:linear-gradient(180deg,#7a2f52,#4e1c35)"></div>
      <p>Tailored Drawstring Cargo Pant<br>Stretch Fabric Plum</p>
      <div class="price"><s>$24.99</s><span>Our Price: $18.99</span></div>
    </div>
    <div class="prod">
      <div class="prod-img" role="img" aria-label="Red scrub top" style="background:linear-gradient(180deg,#b32730,#7e141b)"></div>
      <p>V-Neck Stretch Scrub Top<br>Crimson Red</p>
      <div class="price"><s>$22.99</s><span>Our Price: $16.99</span></div>
    </div>
    <div class="prod">
      <div class="prod-img" role="img" aria-label="Navy scrub pants" style="background:linear-gradient(180deg,#2d3a66,#1a2244)"></div>
      <p>Unisex Straight Leg Scrub Pant<br>Navy Blue</p>
      <div class="price"><s>$26.99</s><span>Our Price: $19.99</span></div>
    </div>
    <div class="prod">
      <div class="prod-img" role="img" aria-label="Khaki scrub top" style="background:linear-gradient(180deg,#c8ae88,#a08663)"></div>
      <p>Men's Classic V-Neck Top<br>Two Pocket Khaki</p>
      <div class="price"><s>$23.99</s><span>Our Price: $17.99</span></div>
    </div>
    <span class="p-arrow r">&#8250;</span>
  </div>
</section>

<section class="promos">
  <div class="promo" role="img" aria-label="Smiling nurse with stethoscope">
    <div class="promo-text"><h3>Want to Receive Discounts</h3><p>SIGN UP FOR OUR EXCLUSIVE EMAILS</p><span class="btn">Shop Now</span></div>
  </div>
  <div class="promo right" role="img" aria-label="Medical team in scrubs">
    <div class="promo-text"><h3>We Make Group Ordering Easy</h3><p>Call Us for Group Ordering</p><span class="btn">Shop Now</span></div>
  </div>
</section>

<section class="about">
  <h2 class="sec-title">About Us</h2>
  <p>We are a California team that believes great shifts begin with clothes that fit well and feel good. Our scrubs use breathable, modern fabrics with a tailored cut so you can move freely from the first round to the last chart. We test every style with working nurses, refine the details they care about, and keep our prices fair. Whether you are outfitting yourself or a whole unit, we make ordering simple, shipping fast and returns easy. Thank you for trusting us to be part of your workday, every single day of the week.</p>
</section>

<section class="why">
  <div class="why-badge"></div>
  <h3>WHY SHOP AT LUMEN WEARWELL</h3>
  <ul>
    <li>Free shipping on every order over fifty</li>
    <li>Tailored fits in soft stretch fabrics</li>
    <li>Easy returns within thirty full days</li>
  </ul>
  <ul>
    <li>Group ordering for clinics and teams</li>
    <li>New colors added every single season</li>
    <li>Friendly support from real people</li>
  </ul>
</section>

<section class="brands">
  <h2 class="sec-title">Shop By Brand</h2>
  <div class="brand-row">
    <span>Harbor</span><span>Vellum</span><span>Coastline</span><span>Brightfold</span><span>Marigold</span><span>Tessa</span>
  </div>
</section>

<section class="newsletter">
  <div class="wrap">
    <div class="nl-title">
      <svg width="40" height="30" viewBox="0 0 40 30"><rect x="1" y="1" width="38" height="28" fill="#fff" stroke="#0255a3" stroke-width="2"/><path d="M1 1l19 15L39 1" fill="none" stroke="#0255a3" stroke-width="2"/></svg>
      <div><h3>Sign Up to Our Newsletters</h3><p>Get the latest styles, news and exclusive offers delivered to you.</p></div>
    </div>
    <div class="nl-form"><div></div><span>SEND</span></div>
  </div>
</section>

<footer class="site-footer">
  <div class="wrap">
    <div class="f-col"><h4>Company Info</h4><ul><li>About Us</li><li>Wholesale</li><li>Careers</li><li>Store Locator</li><li>Contact Us</li></ul></div>
    <div class="f-col"><h4>My Account</h4><ul><li>Sign In</li><li>My Orders</li><li>Track My Order</li><li>Wishlist</li><li>Gift Cards</li></ul></div>
    <div class="f-col"><h4>Policies</h4><ul><li>Return Policy</li><li>Privacy Policy</li><li>Shipping Info</li><li>Size Guide</li><li>Terms of Service</li></ul></div>
    <div class="f-col"><h4>Follow Us</h4><div class="socials"><i></i><i></i><i></i><i></i><i></i><i></i></div></div>
  </div>
</footer>
<div class="copyright">Copyright © Lumen Wearwell. All Rights Reserved. www.tovandrel.com</div>

</body>
</html>
```